Business Card Update, need to bring life to the card, two sided color

We need a new business card design, are moving and changing addresses and need a new look, we have the logos already attached but need a new style moving forward. Can incorporate the color of the logo (The Green) as well, maybe a solid back? We deal with safety products revolving around static electricity and safety lighting. Would like to keep same font in second logo as well.

Target Market(s)

Electrical Safety, Lighting

Contact Information for Business Card

Lars Whitcombe
Vice President
Office: 555-284-7316
Cell: 555-862-0457
lars@tkwhitcombe.com
www.tkwhitcombe.com
4700 West Cedar Boulevard
Suite #320
Roswell, GA 30412

Font styles to use
Serif
Sans Serif

Requirements
Must have
• Since 1918
Nice to have
• Could use the 100 Year Logo for back of card, would like the back of card to be the same green as logo.
Should not have
• No black cards please.

```html
<!DOCTYPE html>
<html lang="en">
<head>
<meta charset="utf-8">
<title>T.K. Whitcombe Business Card</title>
<link rel="stylesheet" href="https://fonts.googleapis.com/css2?family=Open+Sans:wght@400;600;700;800&display=swap">
<style>
  :root {
    --brand-green: #0b8c4c;
    --card-white: #f4f4f3;
    --ink: #4a4a4a;
    --rule: #8a8a8a;
    --backdrop: #e3e1de;
  }
  * { margin: 0; padding: 0; box-sizing: border-box; }
  html, body {
    width: 1200px; height: 1004px; overflow: hidden;
    background: var(--backdrop);
    font-family: "Open Sans", Arial, sans-serif;
  }
  .card {
    position: absolute; left: 220px;
    width: 760px; height: 434px;
    box-shadow: 0 6px 18px rgba(0,0,0,.12);
    overflow: hidden;
  }
  /* Back side */
  .card-back { top: 48px; background: var(--brand-green); color: #fff; }
  .back-mark {
    position: absolute; left: 0; right: 0; top: 150px;
    display: flex; align-items: center; justify-content: center; gap: 18px;
  }
  .back-mark .dot { width: 64px; height: 64px; border-radius: 50%; background: #fff; }
  .back-mark .wordmark { font-weight: 800; font-size: 46px; letter-spacing: .5px; }
  .back-since {
    position: absolute; left: 0; right: 0; top: 252px;
    text-align: center; font-size: 24px; font-weight: 600; letter-spacing: 1px;
  }
  /* Front side */
  .card-front { top: 522px; background: var(--card-white); color: var(--ink); }
  .front-dot {
    position: absolute; left: 48px; top: 70px;
    width: 112px; height: 112px; border-radius: 50%; background: var(--brand-green);
  }
  .company { position: absolute; left: 182px; top: 74px; color: var(--brand-green); }
  .company-name { font-weight: 800; font-size: 44px; line-height: 1; }
  .company-sub { font-weight: 800; font-size: 19px; margin-top: 6px; }
  .person { position: absolute; right: 40px; top: 170px; text-align: right; }
  .person-name { color: var(--brand-green); font-weight: 800; font-size: 26px; line-height: 1.1; }
  .person-rule { position: absolute; left: 182px; right: 40px; top: 208px; height: 1px; background: var(--rule); }
  .person-title { position: absolute; right: 40px; top: 212px; font-size: 17px; color: #6a6a6a; }
  .address { position: absolute; right: 40px; top: 258px; text-align: right; font-size: 17px; line-height: 1.35; font-weight: 600; }
  .contact-rule { position: absolute; left: 40px; width: 260px; top: 290px; height: 1px; background: var(--rule); }
  .contacts { position: absolute; left: 40px; top: 300px; list-style: none; font-size: 17px; line-height: 1.4; }
  .contacts li { display: flex; align-items: center; gap: 8px; }
  .contacts svg { width: 14px; height: 14px; fill: var(--brand-green); flex: none; }
  .edge-band { position: absolute; left: 0; right: 0; bottom: 0; height: 12px; background: var(--brand-green); }
</style>
</head>
<body>

<section class="card card-back" aria-label="Card back">
  <div class="back-mark">
    <span class="dot"></span>
    <span class="wordmark">T.K. Whitcombe</span>
  </div>
  <p class="back-since">Since 1918</p>
</section>

<section class="card card-front" aria-label="Card front">
  <span class="front-dot"></span>
  <div class="company">
    <div class="company-name">T.K. Whitcombe</div>
    <div class="company-sub">Manufacturing Company, Inc.</div>
  </div>
  <div class="person"><div class="person-name">Lars Whitcombe</div></div>
  <div class="person-rule"></div>
  <div class="person-title">Vice President</div>
  <div class="address">4700 West Cedar Boulevard<br>Suite #320 Roswell, GA 30412</div>

  <div class="contact-rule"></div>
  <ul class="contacts">
    <li><svg viewBox="0 0 16 16"><path d="M3 1h3l1 4-2 1c1 2 3 4 5 5l1-2 4 1v3c0 1-1 2-2 2C7 15 1 9 1 3c0-1 1-2 2-2z"/></svg>555-284-7316</li>
    <li><svg viewBox="0 0 16 16"><path d="M4 0h8a1 1 0 0 1 1 1v14a1 1 0 0 1-1 1H4a1 1 0 0 1-1-1V1a1 1 0 0 1 1-1zm1 2v10h6V2z"/></svg>555-862-0457</li>
    <li><svg viewBox="0 0 16 16"><path d="M1 3h14v10H1zm1 1v.5l6 4 6-4V4z"/></svg>lars@tkwhitcombe.com</li>
    <li><svg viewBox="0 0 16 16"><path d="M8 0a8 8 0 1 0 0 16A8 8 0 0 0 8 0zm0 2a6 6 0 0 1 5.7 4H10a9 9 0 0 0-2-4zm0 12a6 6 0 0 1-5.7-4H6a9 9 0 0 0 2 4zM2.3 6H6a9 9 0 0 1 2-4 6 6 0 0 0-5.7 4zm11.4 4H10a9 9 0 0 1-2 4 6 6 0 0 0 5.7-4zM7 7h2v2H7z"/></svg>www.tkwhitcombe.com</li>
  </ul>
  <div class="edge-band"></div>
</section>

</body>
</html>
```